Business Card Design Project - Sports Brand

Lumora is a e-commerce fitness wear brand for ladies who are into gym, pole and swim.

Card should not be overly cluttered and should include the following:

1. logo
2. Name of the company (Use "Lumora Wear Pte Ltd" for now)
3. Address of company (Use a mock address)
4. Representative's name and contact info etc. (use a mock name and contact info)
5. website address

Target Market(s)

Women who are into pole , gym, and swim.

Women who shop online

Industry/Entity Type

E-Commerce

Colors

Designer to choose colors to be used in the design.

Requirements
Nice to have
• feminine sublimation of colours

Need not be printed on traditional paper. We would like the design to be revolutionary and interesting to the eye :)
Should not have
• the design should not be traditional looking. Do not include illustrations of Bikinis, yoga poses etc. in the card.

```html
<!DOCTYPE html>
<html lang="en">
<head>
<meta charset="utf-8">
<title>Lumora Wear – Business Cards</title>
<link rel="stylesheet" href="https://fonts.googleapis.com/css2?family=Cinzel:wght@400&family=Lato:wght@400;700;900&family=Raleway:wght@200&display=swap">
<style>
  :root {
    --stage: #2b2b2b;
    --card: #ffffff;
    --card-shade: #f1f1f1;
    --band-pink: #e17aa6;
    --band-rose: #e54d7b;
    --brand-red: #b81f3a;
    --brand-dot: #ea5a86;
    --ink: #1f1f1f;
    --muted: #666666;
    --icon: #d9457a;
  }
  * { box-sizing: border-box; margin: 0; padding: 0; }
  html, body { width: 1200px; height: 900px; overflow: hidden; }
  body { background: var(--stage); position: relative; font-family: "Lato", sans-serif; }

  .card {
    position: absolute;
    width: 560px;
    height: 320px;
    border-radius: 18px;
    overflow: hidden;
    background: linear-gradient(180deg, var(--card) 0%, var(--card-shade) 100%);
    box-shadow: 0 18px 40px rgba(0,0,0,0.55);
  }
  .card--front { left: 60px; top: 90px; }
  .card--back { left: 580px; top: 490px; }

  /* brand lockup */
  .brand { position: absolute; display: flex; align-items: center; gap: 12px; }
  .brand__dot { width: 46px; height: 46px; border-radius: 50%; background: var(--brand-dot); flex: none; }
  .brand__text { display: flex; flex-direction: column; }
  .brand__name { font-family: "Lato", sans-serif; font-weight: 700; font-size: 44px; line-height: 1; color: var(--brand-red); letter-spacing: 1px; }
  .brand__tagline { font-family: "Lato", sans-serif; font-weight: 400; font-size: 13px; color: var(--muted); margin-top: 4px; letter-spacing: 0.5px; }

  /* front */
  .card--front .brand { left: 120px; top: 92px; }
  .front-band {
    position: absolute; left: 0; right: 0; bottom: 0; height: 78px;
    background: var(--band-pink);
    display: flex; align-items: center; padding-left: 40px;
  }
  .front-band__company { font-family: "Raleway", sans-serif; font-weight: 200; font-size: 34px; color: #ffffff; letter-spacing: 1px; }

  /* back */
  .back-band {
    position: absolute; left: 0; right: 0; top: 0; height: 62px;
    background: linear-gradient(90deg, var(--band-rose) 0%, var(--band-pink) 100%);
    text-align: right; padding: 10px 24px 0 0; color: #ffffff;
  }
  .back-band__name { font-family: "Cinzel", serif; font-size: 20px; line-height: 1.1; letter-spacing: 1px; }
  .back-band__role { font-family: "Lato", sans-serif; font-weight: 700; font-size: 13px; }
  .card--back .brand { left: 180px; top: 88px; }

  .contacts {
    position: absolute; left: 120px; top: 196px;
    display: grid; grid-template-columns: 170px auto; column-gap: 22px; row-gap: 6px;
    font-size: 14px; font-weight: 700; color: var(--ink);
  }
  .contact { display: flex; align-items: center; gap: 7px; white-space: nowrap; }
  .contact svg { width: 14px; height: 14px; fill: var(--icon); flex: none; }
  .contact__accent { color: var(--brand-red); }
  .address { position: absolute; left: 28px; bottom: 22px; }
</style>
</head>
<body>

<section class="card card--front" aria-label="Card front">
  <div class="brand">
    <span class="brand__dot"></span>
    <div class="brand__text">
      <span class="brand__name">Lumora</span>
      <span class="brand__tagline">Yoga · Swim · Pole</span>
    </div>
  </div>
  <div class="front-band">
    <span class="front-band__company">Lumora Wear Pte Ltd</span>
  </div>
</section>

<section class="card card--back" aria-label="Card back">
  <header class="back-band">
    <div class="back-band__name">YOUR NAME</div>
    <div class="back-band__role">Designation</div>
  </header>

  <div class="brand">
    <span class="brand__dot"></span>
    <div class="brand__text">
      <span class="brand__name">Lumora</span>
      <span class="brand__tagline">Yoga · Swim · Pole</span>
    </div>
  </div>

  <div class="contacts">
    <span class="contact">
      <svg viewBox="0 0 16 16" aria-hidden="true"><path d="M2 5c0-2 2-3 3-3l1 3-2 1c1 2 3 4 5 5l1-2 3 1c0 1-1 3-3 3C6 13 2 9 2 5z"/></svg>
      (852) 2345 6789
    </span>
    <span class="contact">
      <svg viewBox="0 0 16 16" aria-hidden="true"><path d="M6 9 10 5l1 1-4 4zM3 9l3-3 1 1-3 3 2 2 3-3 1 1-3 3c-1 1-2 1-3 0L3 12c-1-1-1-2 0-3zm6-6c1-1 2-1 3 0l1 1c1 1 1 2 0 3l-3 3-1-1 3-3-2-2-3 3-1-1z"/></svg>
      <span>www.<span class="contact__accent">lumorawear</span>.com</span>
    </span>
    <span class="contact">
      <svg viewBox="0 0 16 16" aria-hidden="true"><path d="M4 1h8v14H4zM5.5 2.5v10h5v-10z"/></svg>
      (852) 2345 6789
    </span>
    <span class="contact">
      <svg viewBox="0 0 16 16" aria-hidden="true"><path d="M1 3h14v10H1zm1.5 1.5v.3L8 9l5.5-4.2v-.3z"/></svg>
      yourinfo@lumorawear.com
    </span>
  </div>

  <div class="contacts address">
    <span class="contact">
      <svg viewBox="0 0 16 16" aria-hidden="true"><path d="M8 1l7 6h-2v8h-4v-5H7v5H3V7H1z"/></svg>
      18 Willow Crest Avenue #04-22 Harbourline Hub Singapore 538412
    </span>
  </div>
</section>

</body>
</html>
```